877 stay Bold

Redesigning this front and back business card flyer and keeping the info but making it look better.

This is all about using the info and logo on the business card design and creating a better layout using any of the following and more.

Changing the background color or imagine, chaining the placement of content, resizing content.

Target Market(s)

Targeting people that have been injured on one side and people that have been giving a DUI on the other.

Contact Information for Business Card

We are looking to keep the info but make it look a fee cleaner and less cluttered

Font styles to use
Sans Serif

Requirements
Must have
• Must have the same info but a better layout.
Nice to have
• better background colors or image or layout. different fonts or same font all design options that will make it look professional and clean.

```html
<!DOCTYPE html>
<html lang="en">
<head>
<meta charset="utf-8">
<title>877 Stay Bold – Business Card Flyer</title>
<link rel="stylesheet" href="https://fonts.googleapis.com/css2?family=Bebas+Neue&family=Lato:ital,wght@0,400;0,700;0,900;1,400&display=swap">
<style>
  :root{
    --red:#c8232b;
    --red-light:#d9373c;
    --navy:#130a3d;
    --yellow:#ffee00;
    --white:#ffffff;
    --page:#ffffff;
  }
  *{margin:0;padding:0;box-sizing:border-box}
  html,body{width:1200px;height:846px;overflow:hidden;background:var(--page)}
  body{position:relative;font-family:"Lato",sans-serif;color:var(--white)}

  .card{position:absolute;width:600px;height:360px;overflow:hidden;background:var(--navy)}
  .card--injury{left:301px;top:36px}
  .card--dui{left:298px;top:427px}

  /* injury side */
  .injury-header{position:absolute;left:0;top:0;width:600px;height:113px;background:var(--red)}
  .injury-lead{position:absolute;left:38px;top:15px;font-weight:900;font-size:25px;letter-spacing:1px;white-space:nowrap}
  .injury-title{position:absolute;left:38px;top:42px;font-family:"Bebas Neue",sans-serif;font-weight:400;font-size:68px;line-height:1;color:var(--yellow);white-space:nowrap}
  .injury-reasons{position:absolute;left:336px;top:24px;list-style:none}
  .injury-reasons li{display:flex;align-items:center;gap:7px;font-weight:700;font-size:14.8px;height:20.5px;white-space:nowrap}
  .alert-icon{width:14px;height:14px;flex:none}

  .photo-strip{position:absolute;left:0;top:113px;width:600px;height:109px}
  .photo{position:absolute;top:0;height:109px}
  .photo--crash{left:0;width:198px;background:linear-gradient(135deg,#9fb2c2 0%,#5f6b78 45%,#1f2533 100%)}
  .photo--knee{left:201px;width:199px;background:linear-gradient(135deg,#7d8fbf 0%,#cfe6ee 45%,#3a3f55 100%)}
  .photo--wheelchair{left:403px;width:197px;background:linear-gradient(120deg,#4a4d55 0%,#d7dde2 55%,#eef2f4 100%)}

  /* shared brand block */
  .brand{position:absolute;left:0;width:600px;display:flex;justify-content:center;align-items:center;gap:12px}
  .brand-mark{width:22px;height:22px;background:var(--red);flex:none}
  .brand-name{font-weight:900;font-size:44px;color:var(--white);letter-spacing:.5px;line-height:1;text-transform:uppercase;white-space:nowrap}
  .card--injury .brand{top:238px}
  .card--dui .brand{top:254px}

  .contact{position:absolute;left:0;width:600px;display:flex;justify-content:center;align-items:center;font-size:19px;white-space:nowrap}
  .contact-call{display:flex;align-items:baseline;gap:6px}
  .contact-phone{font-weight:900;font-size:29px;color:var(--yellow)}
  .contact-divider{width:1px;height:28px;background:rgba(255,255,255,.55);margin:0 18px}
  .contact-web b{font-weight:900}
  .card--injury .contact{top:289px}
  .card--dui .contact{top:309px}

  .tagline-ribbon{position:absolute;left:0;top:329px;width:590px;height:20px}
  .tagline-ribbon svg{position:absolute;inset:0}
  .tagline-text{position:absolute;left:0;top:0;width:590px;height:20px;line-height:20px;text-align:center;font-weight:900;font-size:12.5px;letter-spacing:2px;white-space:nowrap}

  /* DUI side */
  .dui-backdrop{position:absolute;left:330px;top:95px;width:290px;height:270px;border-radius:50% 0 0 0;background:radial-gradient(ellipse at 55% 45%,#2e2570 0%,#1a1150 50%,rgba(19,10,61,0) 75%)}
  .dui-title-band{position:absolute;left:0;top:23px;width:600px;height:44px;background:var(--red)}
  .dui-title{position:absolute;left:43px;top:3px;font-family:"Bebas Neue",sans-serif;font-weight:400;font-size:42px;line-height:1;color:var(--yellow);white-space:nowrap}
  .dui-question-band{position:absolute;left:0;top:70px;width:600px;height:27px;background:var(--red-light)}
  .dui-question{position:absolute;right:31px;top:1px;font-weight:900;font-size:21.5px;white-space:nowrap}
  .dui-steps{position:absolute;left:46px;top:104px;list-style:none}
  .dui-steps li{display:flex;align-items:flex-start;gap:6px;font-weight:700;font-size:14.8px;line-height:19.6px;white-space:nowrap}
  .dui-steps .alert-icon{margin-top:2px}
  .dui-steps em{font-weight:400}
</style>
</head>
<body>

<svg width="0" height="0" style="position:absolute">
  <defs>
    <symbol id="alert-dark" viewBox="0 0 14 14">
      <path d="M7 1 L13.4 13 H0.6 Z" fill="#130a3d" stroke="#130a3d" stroke-linejoin="round"/>
      <rect x="6.2" y="5" width="1.6" height="4.3" fill="#ffee00"/>
      <rect x="6.2" y="10.2" width="1.6" height="1.5" fill="#ffee00"/>
    </symbol>
    <symbol id="alert-red" viewBox="0 0 14 14">
      <path d="M7 1 L13.4 13 H0.6 Z" fill="#e2262e" stroke="#e2262e" stroke-linejoin="round"/>
      <rect x="6.2" y="5" width="1.6" height="4.3" fill="#fff"/>
      <rect x="6.2" y="10.2" width="1.6" height="1.5" fill="#fff"/>
    </symbol>
  </defs>
</svg>

<section class="card card--injury">
  <header class="injury-header">
    <p class="injury-lead">If you've been injured</p>
    <h1 class="injury-title">STAY BOLD</h1>
    <ul class="injury-reasons">
      <li><svg class="alert-icon"><use href="#alert-dark"/></svg>for an inexperienced lawyer!</li>
      <li><svg class="alert-icon"><use href="#alert-dark"/></svg>for less than you deserve!</li>
      <li><svg class="alert-icon"><use href="#alert-dark"/></svg>for paying massive medical bills!</li>
      <li><svg class="alert-icon"><use href="#alert-dark"/></svg>for a life of pain and debt!</li>
    </ul>
  </header>

  <div class="photo-strip">
    <div class="photo photo--crash" role="img" aria-label="Photo of a damaged car after a road collision"></div>
    <div class="photo photo--knee" role="img" aria-label="Photo of a bandaged knee in a brace on a hospital bed"></div>
    <div class="photo photo--wheelchair" role="img" aria-label="Photo of an injured man in a wheelchair by a window"></div>
  </div>

  <div class="brand">
    <span class="brand-name">877 Stay Bold</span>
    <span class="brand-mark"></span>
  </div>

  <div class="contact">
    <span class="contact-call">Call <span class="contact-phone">877-555-0142</span></span>
    <span class="contact-divider"></span>
    <span class="contact-web">www.<b>877staybold</b>.com</span>
  </div>

  <div class="tagline-ribbon">
    <svg width="590" height="20" viewBox="0 0 590 20">
      <defs>
        <linearGradient id="ribbon-fill" x1="0" x2="1">
          <stop offset="0" stop-color="#e0423f"/>
          <stop offset="1" stop-color="#c8232b"/>
        </linearGradient>
      </defs>
      <path d="M0 0 H580 L590 10 L580 20 H0 Z" fill="url(#ribbon-fill)"/>
    </svg>
    <p class="tagline-text">WE FIGHT FOR YOU, SO YOU CAN FOCUS ON GETTIG BETTER</p>
  </div>
</section>

<section class="card card--dui">
  <div class="dui-backdrop" role="img" aria-label="Faint photo of a judge's gavel"></div>

  <div class="dui-title-band">
    <h2 class="dui-title">STAY BOLD AGAINST A DUI</h2>
  </div>
  <div class="dui-question-band">
    <p class="dui-question">what should I do if I get pulled over for DUI?</p>
  </div>

  <ul class="dui-steps">
    <li><svg class="alert-icon"><use href="#alert-red"/></svg>Put over in a calm, normal manner</li>
    <li><svg class="alert-icon"><use href="#alert-red"/></svg>Be polite at all times</li>
    <li><svg class="alert-icon"><use href="#alert-red"/></svg>Do not admit to drinking</li>
    <li><svg class="alert-icon"><use href="#alert-red"/></svg>Do not submit to any field sobriety tests</li>
    <li><svg class="alert-icon"><use href="#alert-red"/></svg><span>Do not submit to taking a chemical test <em>(breath, blood, or urine)</em></span></li>
    <li><svg class="alert-icon"><use href="#alert-red"/></svg><span>Do notmake any statement after being arrested,<br>especially when placed in the police cruiser</span></li>
  </ul>

  <div class="brand">
    <span class="brand-name">877 Stay Bold</span>
    <span class="brand-mark"></span>
  </div>

  <div class="contact">
    <span class="contact-call">Call <span class="contact-phone">877-555-0142</span></span>
    <span class="contact-divider"></span>
    <span class="contact-web">www.<b>877staybold</b>.com</span>
  </div>
</section>

</body>
</html>
```